20 years old IT solutions company needs brand new corporate style.

We are based in Latvia. Our business is ERP systems implementation, IT infrastructure building and supporting our customers. We are moving from traditional Add-hoc projects model to standardized flat-rate offerings. Our technology platform is Quorvanel. The value proposition of our offerings is based around simplicity, transparency, quality, peace of mind, trust, easy of doing business.
We have created the new logo and now we expect to have full stationary with both color palette and fonts which must be unicode (to ensure proper Latvian language characters display)

Target Market(s)

Small and Medium Enterprise

Requirements
Must have
• Would like to to see not only B&W but colored versions as well.

```html
<!DOCTYPE html>
<html lang="en">
<head>
<meta charset="utf-8">
<title>Business Card Print Guide</title>
<link href="https://fonts.googleapis.com/css2?family=Signika:wght@400;600&family=Roboto:wght@300;400;500;700&display=swap" rel="stylesheet">
<style>
:root{
  --bg:#e6e7e9;
  --paper:#ffffff;
  --ink:#111111;
  --grey:#6d6e71;
  --light-grey:#b8babd;
  --bleed-blue:#aadcf5;
  --trim-blue:#9fd3e8;
  --safe-pink:#f4b6cf;
  --bleed-pink:#ec407a;
  --safe-green:#8cc98c;
  --crop-red:#b3262f;
  --teal:#16b4b4;
  --lime:#8cc63f;
  --yellow:#ffc60b;
}
*{margin:0;padding:0;box-sizing:border-box}
html,body{width:1021px;height:1200px;overflow:hidden;background:var(--bg)}
body{position:relative;font-family:"Roboto",sans-serif;color:var(--ink)}
.abs{position:absolute}
.sheet{position:absolute;background:var(--paper);box-shadow:6px 8px 10px rgba(0,0,0,.28)}

/* spec sheet */
.spec{left:347px;top:139px;width:326px;height:214px}
.bleed-area{left:38px;top:0;width:286px;height:172px;background:var(--bleed-blue);border:1px solid #8fc3de}
.safe-area{left:47px;top:10px;width:268px;height:154px;background:var(--safe-pink);border:1px solid #c97a9c}
.live-area{left:56px;top:20px;width:250px;height:134px;background:var(--paper);border:1px dashed #c97a9c}
.spec-title{left:38px;width:286px;top:46px;text-align:center;font-family:"Signika",sans-serif;font-weight:600;font-size:13.5px;line-height:17px}
.spec-size{left:38px;width:286px;top:84px;text-align:center;font-family:"Signika",sans-serif;font-weight:600;font-size:26px}
.zone-note{width:286px;left:38px;text-align:center;font-family:"Signika",sans-serif;font-weight:600;font-size:5px;letter-spacing:-.1px}
.dim-text{font-family:"Signika",sans-serif;font-weight:600;font-size:13px;background:var(--paper);padding:0 5px}
.dim-faint{font-family:"Signika",sans-serif;font-size:7px;color:var(--light-grey);background:var(--paper);padding:0 4px}

/* guide sheet */
.guide{left:347px;top:373px;width:323px;height:248px}
.guide h1{position:absolute;left:18px;top:13px;font-size:12px;font-weight:700}
.guide-intro{left:18px;top:34px;font-size:5.6px;color:var(--grey);font-weight:300}
.guide-label{left:18px;font-size:12px;font-weight:500}
.guide-copy{left:18px;width:112px;font-size:5.8px;line-height:11.4px;color:var(--grey);font-weight:300}
.label-bleed{color:var(--bleed-pink)}
.label-trim{color:var(--trim-blue)}
.label-safe{color:var(--safe-green)}
.diagram-num{font-size:5.5px;font-weight:700}
.other-sizes{left:147px;top:205px;font-size:6px;line-height:11.4px;color:var(--grey);font-weight:300}
.other-sizes b{color:var(--ink);font-weight:700}
.other-sizes span{color:#8a8c8f;font-weight:500}

/* business card */
.card{width:276px;height:166px;background:var(--paper);box-shadow:6px 8px 10px rgba(0,0,0,.28)}
.card-print{left:363px;top:659px}
.card-final{left:382px;top:914px;width:257px;height:147px}
.brand{display:flex;align-items:center;gap:4px}
.brand-square{width:9px;height:9px;border:1.6px solid var(--ink)}
.brand-name{font-family:"Roboto",sans-serif;font-weight:700;font-size:10.5px;line-height:10px;letter-spacing:1.2px;color:var(--ink)}
.holder{text-align:right}
.holder-name{font-weight:700;font-size:8.6px;line-height:10px}
.holder-role{font-size:8px;line-height:10px}
.contacts{font-size:8px;line-height:10.4px;font-weight:400}
.contacts li{list-style:none;display:flex;align-items:center;gap:3px}
.contacts svg{width:6.5px;height:6.5px}
.address{text-align:right;font-size:8px;line-height:10.4px}
.colour-bar{display:flex;gap:1.5px;left:0;right:0;bottom:0}
.colour-bar i{display:block;height:100%}
.bar-black{background:var(--ink)}
.bar-teal{background:var(--teal)}
.bar-lime{background:var(--lime)}
.bar-yellow{background:var(--yellow)}
.crop{background:var(--crop-red)}
.final-caption{left:0;width:1021px;top:887px;text-align:center;font-size:11.5px;font-weight:400;letter-spacing:.1px}
</style>
</head>
<body>

<!-- dimension spec sheet -->
<section class="sheet spec">
  <div class="abs bleed-area"></div>
  <div class="abs safe-area"></div>
  <div class="abs live-area"></div>
  <p class="abs spec-title">Standard Business Card<br>Finished Dimensions</p>
  <p class="abs spec-size">3.5″ x 2″</p>
  <p class="abs zone-note" style="top:155px">PINK: SAFE ZONE - NO TEXT OR CRITICAL INFORMATION SHOULD TOUCH THIS AREA</p>
  <p class="abs zone-note" style="top:165px">BLUE: BLEED AREA</p>

  <svg class="abs" style="left:0;top:0" width="38" height="214" viewBox="0 0 38 214">
    <g stroke="#222" stroke-width="1"><line x1="23" y1="10" x2="23" y2="163"/><line x1="18" y1="10" x2="28" y2="10"/><line x1="18" y1="163" x2="28" y2="163"/></g>
    <g stroke="#c9cbcd" stroke-width="1"><line x1="4" y1="0" x2="4" y2="172"/><line x1="0" y1="172" x2="9" y2="172"/></g>
    <rect x="17" y="48" width="12" height="72" fill="#fff"/>
    <rect x="0" y="52" width="9" height="64" fill="#fff"/>
    <text transform="translate(18.5 52) rotate(90)" font-family="Signika, sans-serif" font-weight="600" font-size="13">2″ Finished</text>
    <text transform="translate(2 55) rotate(90)" font-family="Signika, sans-serif" font-size="6.5" fill="#b8babd">2.25″ with Bleed</text>
  </svg>

  <svg class="abs" style="left:38px;top:182px" width="288" height="32" viewBox="0 0 288 32">
    <g stroke="#222" stroke-width="1"><line x1="9" y1="8" x2="277" y2="8"/><line x1="9" y1="3" x2="9" y2="13"/><line x1="277" y1="3" x2="277" y2="13"/></g>
    <g stroke="#c9cbcd" stroke-width="1"><line x1="0" y1="26" x2="286" y2="26"/><line x1="0" y1="21" x2="0" y2="31"/><line x1="286" y1="21" x2="286" y2="31"/></g>
  </svg>
  <span class="abs dim-text" style="left:141px;top:182px">3.5″ Finished</span>
  <span class="abs dim-faint" style="left:152px;top:203px">3.75″ with Bleed</span>
</section>

<!-- bleed / trim / safe explanation -->
<section class="sheet guide">
  <h1>How a 3.5”x2” Business Card should look.</h1>
  <p class="abs guide-intro">This is how a 3.5”x2” card.. The bleeds are 0.125” thick on all sides, so the card measures 3.75x2.25 inch</p>

  <p class="abs guide-label label-bleed" style="top:55px">Bleeds</p>
  <p class="abs guide-copy" style="top:75px">The background and non-<br>critical elements of a design<br>should extend to this line.</p>
  <p class="abs guide-label label-trim" style="top:113px">Trim Line</p>
  <p class="abs guide-copy" style="top:133px">The final size of the file and<br>the line to which the printed<br>card will be cut.</p>
  <p class="abs guide-label label-safe" style="top:172px">Safe Zone</p>
  <p class="abs guide-copy" style="top:192px;width:120px">Any text, logos or content<br>placed in this area is entirely safe.<br>You should place important info away<br>from the trim line within the safe zone.</p>

  <svg class="abs" style="left:0;top:0" width="323" height="248" viewBox="0 0 323 248">
    <rect x="120.5" y="55.5" width="193" height="129" fill="none" stroke="#ec407a" stroke-width="1"/>
    <rect x="129.5" y="65.5" width="175" height="108" fill="none" stroke="#9fd3e8" stroke-width="1"/>
    <rect x="139.5" y="75.5" width="156" height="88" fill="none" stroke="#8cc98c" stroke-width="1"/>
    <line x1="61" y1="62" x2="120" y2="62" stroke="#ec407a" stroke-width=".7"/>
    <line x1="76" y1="121" x2="129" y2="121" stroke="#9fd3e8" stroke-width=".7"/>
    <polyline points="80,180 149,180 149,163" fill="none" stroke="#8cc98c" stroke-width=".7"/>
  </svg>
  <span class="abs diagram-num" style="left:207px;top:57px">0.125”</span>
  <span class="abs diagram-num" style="left:124px;top:123px">0.125”</span>
  <span class="abs diagram-num" style="left:293px;top:123px">0.125”</span>
  <span class="abs diagram-num" style="left:204px;top:118px">3.5”x2”</span>
  <span class="abs diagram-num" style="left:207px;top:176px">0.125”</span>

  <p class="abs other-sizes"><b>For other document sizes:</b><br><span>Flyer (8.5x11)</span> the file should measure 8.75x11.25<br><span>Flyer (8.5x11)</span> the file should measure 8.75x11.25</p>
</section>

<!-- card with bleed and crop marks -->
<article class="abs card card-print">
  <div class="abs brand" style="left:30px;top:34px"><span class="brand-square"></span><span class="brand-name">LUMEN<br>ARBOR</span></div>
  <div class="abs holder" style="right:30px;top:39px"><p class="holder-name">ELIAS BRANTMORE</p><p class="holder-role">Managing Director</p></div>
  <ul class="abs contacts" style="left:30px;top:103px">
    <li><svg viewBox="0 0 10 10"><path d="M1 3.5C1 2 3 1 5 1s4 1 4 2.5L7.5 4.2 7 3H3l-.5 1.2zM2.5 5h5L9 9H1z" fill="#111"/></svg>555.204.7180</li>
    <li><svg viewBox="0 0 10 10"><rect x="0.5" y="2" width="9" height="6.5" fill="#111"/><path d="M1 2.5l4 3 4-3" fill="none" stroke="#fff" stroke-width=".9"/></svg>ann@lumenarbor.com</li>
    <li><svg viewBox="0 0 10 10"><circle cx="5" cy="5" r="4.3" fill="none" stroke="#111" stroke-width="1.2"/><path d="M3 2.5l2 1.5-1 2 1.5 2.5M6.5 2l1 2" stroke="#111" stroke-width="1.3" fill="none"/></svg>www.lumenarbor.com</li>
  </ul>
  <p class="abs address" style="right:30px;top:113px">Alder Crest Avenue,<br>Suite 210 Westbrook</p>
  <div class="abs colour-bar" style="height:17px"><i class="bar-black" style="width:154px"></i><i class="bar-teal" style="width:35px"></i><i class="bar-lime" style="width:36px"></i><i class="bar-yellow" style="flex:1"></i></div>
</article>
<div class="abs crop" style="left:331px;top:667px;width:357px;height:1px"></div>
<div class="abs crop" style="left:333px;top:814px;width:357px;height:1px"></div>
<div class="abs crop" style="left:372px;top:641px;width:1px;height:204px"></div>
<div class="abs crop" style="left:629px;top:647px;width:1px;height:201px"></div>

<p class="abs final-caption">FINAL DESIGN AFTER PRINT</p>

<!-- trimmed card -->
<article class="abs card card-final">
  <div class="abs brand" style="left:21px;top:21px"><span class="brand-square"></span><span class="brand-name">LUMEN<br>ARBOR</span></div>
  <div class="abs holder" style="right:21px;top:30px"><p class="holder-name">ELIAS BRANTMORE</p><p class="holder-role">Managing Director</p></div>
  <ul class="abs contacts" style="left:21px;top:95px">
    <li><svg viewBox="0 0 10 10"><path d="M1 3.5C1 2 3 1 5 1s4 1 4 2.5L7.5 4.2 7 3H3l-.5 1.2zM2.5 5h5L9 9H1z" fill="#111"/></svg>555.204.7180</li>
    <li><svg viewBox="0 0 10 10"><rect x="0.5" y="2" width="9" height="6.5" fill="#111"/><path d="M1 2.5l4 3 4-3" fill="none" stroke="#fff" stroke-width=".9"/></svg>ann@lumenarbor.com</li>
    <li><svg viewBox="0 0 10 10"><circle cx="5" cy="5" r="4.3" fill="none" stroke="#111" stroke-width="1.2"/><path d="M3 2.5l2 1.5-1 2 1.5 2.5M6.5 2l1 2" stroke="#111" stroke-width="1.3" fill="none"/></svg>www.lumenarbor.com</li>
  </ul>
  <p class="abs address" style="right:21px;top:105px">Alder Crest Avenue,<br>Suite 210 Westbrook</p>
  <div class="abs colour-bar" style="height:7px"><i class="bar-black" style="width:145px"></i><i class="bar-teal" style="width:35px"></i><i class="bar-lime" style="width:35px"></i><i class="bar-yellow" style="flex:1"></i></div>
</article>

</body>
</html>
```